quorvaAgency Business Card Design Project

We need a business card design for quorvaAgency. quorvaAgency is an underwriting agency. Underwriting agencies act on behalf of insurers, to underwrite insurance. We will be operating in specialised classes of insurance initially and looking to expand from there. We would like to see designs that incorporate our logo colours as well as a contrasting stand out colour - also we'd like the logo itself to be embossed on the card.

Industry/Entity Type

Insurance

Requirements
Must have
• Logo on front
Nice to have
• Logo solely featured on back of card
Should not have
• Please do not use comic cans font :)

```html
<!DOCTYPE html>
<html lang="en">
<head>
<meta charset="utf-8">
<title>quorvaAgency Business Cards</title>
<link rel="stylesheet" href="https://fonts.googleapis.com/css2?family=Arimo:wght@400;700&display=swap">
<style>
  :root {
    --brand-blue: #1b5aa8;
    --ink: #2b2b2b;
    --mark-grey: #3c3f44;
    --card-white: #ffffff;
    --backdrop: #e9e7e4;
  }
  * { box-sizing: border-box; margin: 0; padding: 0; }
  html, body { width: 1200px; height: 900px; overflow: hidden; }
  body {
    background: var(--backdrop);
    font-family: "Arimo", Arial, sans-serif;
    position: relative;
  }
  .card {
    position: absolute;
    width: 538px;
    height: 308px;
    border-radius: 16px;
    background: var(--card-white);
    overflow: hidden;
    box-shadow: 0 2px 6px rgba(0,0,0,0.18);
  }
  .card--front-a { left: 43px; top: 131px; }
  .card--back-a  { left: 625px; top: 131px; }
  .card--front-b { left: 43px; top: 497px; }
  .card--back-b  { left: 625px; top: 497px; background: var(--brand-blue); }

  .band {
    position: absolute;
    left: 0; right: 0; bottom: 0;
    height: 20px;
    background: var(--brand-blue);
  }

  .front-name-mark {
    position: absolute;
    left: 28px; top: 22px;
    font-size: 44px;
    font-weight: 700;
    color: var(--brand-blue);
    letter-spacing: -0.5px;
  }
  .person {
    position: absolute;
    left: 28px; top: 100px;
  }
  .person__name {
    font-size: 25px;
    font-weight: 700;
    color: var(--brand-blue);
    line-height: 1;
  }
  .person__role {
    font-size: 17px;
    color: var(--ink);
    margin-top: 3px;
  }
  .contacts {
    position: absolute;
    left: 26px; top: 172px;
    list-style: none;
  }
  .contacts li {
    display: flex;
    align-items: center;
    gap: 6px;
    font-size: 18px;
    color: var(--ink);
    height: 22px;
  }
  .contacts svg { width: 18px; height: 16px; fill: var(--ink); }

  .front-disc {
    position: absolute;
    left: 390px; top: 160px;
    width: 160px; height: 160px;
    border-radius: 50%;
    background: var(--mark-grey);
  }

  .back-lockup {
    position: absolute;
    left: 0; right: 0; top: 78px;
    display: flex;
    flex-direction: column;
    align-items: center;
    gap: 12px;
  }
  .back-lockup__disc {
    width: 78px; height: 78px;
    border-radius: 50%;
    background: var(--mark-grey);
  }
  .back-lockup__name {
    font-size: 50px;
    font-weight: 700;
    color: var(--brand-blue);
    letter-spacing: -0.5px;
    line-height: 1;
  }
  .card--back-b .back-lockup__disc { background: var(--card-white); }
  .card--back-b .back-lockup__name { color: var(--card-white); }

  .web {
    position: absolute;
    right: 28px; bottom: 3px;
    font-size: 13px;
    color: var(--card-white);
  }
  .card--back-b .web { bottom: 6px; left: 0; right: 0; text-align: center; }
</style>
</head>
<body>

  <section class="card card--front-a">
    <div class="front-name-mark">quorvaAgency</div>
    <div class="person">
      <p class="person__name">Daniel Hart</p>
      <p class="person__role">IT Manager</p>
    </div>
    <ul class="contacts">
      <li><svg viewBox="0 0 18 16"><path d="M1 6c0-3 3-4 8-4s8 1 8 4l-3 1-1-2H5L4 7 1 6zm3 2h10l2 7H2z"/></svg>: 400-5550-1928</li>
      <li><svg viewBox="0 0 18 16"><rect x="5" y="0" width="8" height="16" rx="1.5"/><rect x="7" y="2" width="4" height="6" fill="#fff"/></svg>: 400-5550-7364</li>
      <li><svg viewBox="0 0 18 16"><path d="M1 3h16v11H1zM2.5 4.5 9 9.5l6.5-5v-0.5H2.5z" fill-rule="evenodd"/></svg>: daniel@quorvaagency.com.au</li>
    </ul>
    <div class="band"></div>
    <div class="front-disc"></div>
  </section>

  <section class="card card--back-a">
    <div class="back-lockup">
      <div class="back-lockup__disc"></div>
      <div class="back-lockup__name">quorvaAgency</div>
    </div>
    <div class="band"></div>
    <div class="web">www.quorvaagency.com.au</div>
  </section>

  <section class="card card--front-b">
    <div class="front-name-mark">quorvaAgency</div>
    <div class="person">
      <p class="person__name">Daniel Hart</p>
      <p class="person__role">IT Manager</p>
    </div>
    <ul class="contacts">
      <li><svg viewBox="0 0 18 16"><path d="M1 6c0-3 3-4 8-4s8 1 8 4l-3 1-1-2H5L4 7 1 6zm3 2h10l2 7H2z"/></svg>: 400-5550-1928</li>
      <li><svg viewBox="0 0 18 16"><rect x="5" y="0" width="8" height="16" rx="1.5"/><rect x="7" y="2" width="4" height="6" fill="#fff"/></svg>: 400-5550-7364</li>
      <li><svg viewBox="0 0 18 16"><path d="M1 3h16v11H1zM2.5 4.5 9 9.5l6.5-5v-0.5H2.5z" fill-rule="evenodd"/></svg>: daniel@quorvaagency.com.au</li>
    </ul>
    <div class="band"></div>
    <div class="front-disc"></div>
  </section>

  <section class="card card--back-b">
    <div class="back-lockup">
      <div class="back-lockup__disc"></div>
      <div class="back-lockup__name">quorvaAgency</div>
    </div>
    <div class="web">www.quorvaagency.com.au</div>
  </section>

</body>
</html>
```